Lumo Bathrooms Facelift. Moving the business in to the next professional level.

I'm currently revamping my bathroom renovation business. Part of this revamp includes our marketing strategy to better position ourselves as a professional business. As the name suggests, we primarily do bathroom renovations of all shapes, sizes and budgets. I'd like a business card design that is simple, yet displays our company as sophisticated.
What I'd like is to have a card that incorporates the following elements;
- Orange set as the primary colour and Charcoal/Grey as a complement colour. The card can also include white and/or black.
- I'd like a hexagon pattern within the charcoal/grey (In gloss perhaps to break it up a bit)
- I only want the Lumo Bathrooms logo on the front of the card
- Back of the card would include contact details
- The bottom edges of the card would be rounded off
- I've attached the company name. I'd like to keep lumo as it is. Bathrooms can be modified
Industry/Entity Type
Marketing

```html
<!DOCTYPE html>
<html lang="en">
<head>
<meta charset="utf-8">
<title>Lumo Bathrooms – Business Card</title>
<link href="https://fonts.googleapis.com/css2?family=Saira:wght@400;500;700&display=swap" rel="stylesheet">
<style>
  :root {
    --backdrop: #e4e4e4;
    --card: #ffffff;
    --orange: #f07d1a;
    --charcoal: #3b3e40;
    --grey: #6e7273;
    --text: #333333;
    --band-text: #ffffff;
  }
  * { margin: 0; padding: 0; box-sizing: border-box; }
  html, body { width: 1189px; height: 1200px; overflow: hidden; }
  body {
    background: var(--backdrop);
    font-family: "Saira", sans-serif;
    position: relative;
  }
  .card {
    position: absolute;
    left: 170px;
    width: 856px;
    height: 488px;
    background: var(--card);
    border-radius: 0 0 26px 26px;
    overflow: hidden;
  }
  .card--front { top: 67px; }
  .card--back { top: 626px; }

  .wordmark { position: absolute; text-align: right; font-weight: 400; line-height: 1; }
  .wordmark__name { display: block; color: var(--orange); }
  .wordmark__sub { display: block; color: var(--charcoal); }

  .card--front .wordmark { left: 190px; top: 120px; width: 472px; }
  .card--front .wordmark__name { font-size: 168px; letter-spacing: 14px; margin-right: -14px; }
  .card--front .wordmark__sub { font-size: 42px; letter-spacing: 3px; margin-top: -6px; margin-right: -3px; }

  .card--back .wordmark { left: 40px; top: 160px; width: 340px; }
  .card--back .wordmark__name { font-size: 122px; letter-spacing: 10px; margin-right: -10px; }
  .card--back .wordmark__sub { font-size: 31px; letter-spacing: 2px; margin-top: -2px; margin-right: -2px; }

  .divider {
    position: absolute;
    left: 426px; top: 80px;
    width: 1px; height: 310px;
    background: #c9c9c9;
  }
  .person { position: absolute; left: 472px; top: 88px; }
  .person__name { font-size: 40px; font-weight: 700; letter-spacing: 1px; line-height: 1.1; color: var(--charcoal); }
  .person__role { font-size: 27px; font-weight: 500; letter-spacing: 1px; line-height: 1.25; color: var(--orange); }

  .contacts { position: absolute; left: 472px; top: 244px; list-style: none; }
  .contacts li {
    display: flex; align-items: center;
    height: 32px; font-size: 28px; color: var(--text);
    letter-spacing: 0.5px;
  }
  .contacts .icon {
    width: 26px; height: 26px; margin-right: 20px;
    background: var(--orange); flex-shrink: 0;
  }
  .address-band {
    position: absolute; left: 0; bottom: 0;
    width: 100%; height: 56px;
    background: var(--charcoal);
    border-top: 4px solid var(--orange);
    color: var(--band-text);
    font-size: 26px; letter-spacing: 1.5px;
    display: flex; align-items: center; justify-content: center;
  }
  .address-band__hex { position: absolute; inset: 0; width: 100%; height: 100%; }
  .address-band__text { position: relative; }
</style>
</head>
<body>
  <section class="card card--front" aria-label="Card front">
    <div class="wordmark">
      <span class="wordmark__name">lumo</span>
      <span class="wordmark__sub">BATHROOMS</span>
    </div>
  </section>

  <section class="card card--back" aria-label="Card back">
    <div class="wordmark">
      <span class="wordmark__name">lumo</span>
      <span class="wordmark__sub">BATHROOMS</span>
    </div>
    <div class="divider"></div>
    <div class="person">
      <p class="person__name">Employee Name</p>
      <p class="person__role">Managing Director</p>
    </div>
    <ul class="contacts">
      <li>
        <svg class="icon" viewBox="0 0 26 26" aria-hidden="true"><path d="M6 9c0-2 3-3 7-3s7 1 7 3l-3 1-1-2h-6l-1 2zM8 12h10l2 8H6z" fill="#fff"/><circle cx="13" cy="16" r="2" fill="#f07d1a"/></svg>
        000-000-0000
      </li>
      <li>
        <svg class="icon" viewBox="0 0 26 26" aria-hidden="true"><rect x="8" y="5" width="10" height="6" fill="#fff"/><rect x="5" y="11" width="16" height="7" fill="#fff"/><rect x="8" y="16" width="10" height="5" fill="#fff" stroke="#f07d1a"/></svg>
        000-000-0000
      </li>
      <li>
        <svg class="icon" viewBox="0 0 26 26" aria-hidden="true"><g fill="none" stroke="#fff" stroke-width="1.4"><circle cx="13" cy="13" r="8"/><ellipse cx="13" cy="13" rx="3.5" ry="8"/><path d="M5 13h16M6.5 9h13M6.5 17h13"/></g></svg>
        www.lumosite.test
      </li>
      <li>
        <svg class="icon" viewBox="0 0 26 26" aria-hidden="true"><g fill="none" stroke="#fff" stroke-width="1.4"><rect x="5" y="8" width="16" height="11"/><path d="M5 8l8 6 8-6M5 19l6-5M21 19l-6-5"/></g></svg>
        You@lumomail.test
      </li>
    </ul>
    <div class="address-band">
      <svg class="address-band__hex" aria-hidden="true">
        <defs>
          <pattern id="hex-grid" width="24" height="41.57" patternUnits="userSpaceOnUse">
            <path d="M6 0h12l6 10.39-6 10.39H6L0 10.39zM6 20.78 0 31.18 6 41.57M18 20.78l6 10.39-6 10.4"
                  fill="none" stroke="rgba(255,255,255,0.1)" stroke-width="1"/>
          </pattern>
        </defs>
        <rect width="100%" height="100%" fill="url(#hex-grid)"/>
      </svg>
      <span class="address-band__text">Your Address Inc 2nd Lane Ave Marlowe, NJ 00000</span>
    </div>
  </section>
</body>
</html>
```